Coaching company requires a Bi-Fold Services Brochure

**Please also read attached design brief***

As part of our expanding sales role for our Professional Development Company, we need a Bi-Fold services brochure that offers our clients some further information about our specific services.

This services brochure will be the document that our clients will receive after our initial contact with them so the overall design of this document will play an instrumental part in our securing of ongoing work.

We have prepared a design brief for designers that want to undertake this task and this document should help to clarify any missing information from this online brief. Any designer who is interested in submitting a design should also refer to this attached document to get the full scope of the works required.

Regular email correspondence will also be available to clarify any questions that the design may have

*** Please also note that the finished design will need to be submitted in a PSD format to allow for editing in Photoshop CS6

Target Market(s)

Our target market is Business to Business. We are specifically targeting small, medium and large businesses who are looking to invest in Professional Development for their business and their staff.
The areas of major focus are 1 on 1 coaching of leaders, executives & business owners and group facilitation sessions with their staff.

Industry/Entity Type

Business Service

Font styles to use
Sans Serif

Requirements
Must have
• - Design needs to be an A4 Bi-Fold layout so should suit an A3 sheet of paper (297mm x 420mm)
• - Include our corporate color scheme
• - Finished design must be in PSD format or format that can be edited in Photshop CS6
• - Appealing to small, medium and large businesses (universal appeal)
• - The project must be in CMYK Colour and no less than 300 pixel resolution
Nice to have
• - Our logo incorporated into the front page
• - We would like the images used in this brochure to be happy and vibrant (i.e. smiling faces and energetic etc.)

```html
<!DOCTYPE html>
<html lang="en">
<head>
<meta charset="utf-8">
<title>Testimonials – Veridian PD</title>
<link rel="stylesheet" href="https://fonts.googleapis.com/css2?family=Oswald:wght@600&family=Roboto+Condensed:ital,wght@0,400;0,700;1,400;1,700&family=Montserrat:wght@400;700&display=swap">
<style>
:root{
  --backdrop:#ffffff;
  --paper:#f2f2f4;
  --paper-band:#e6e7ea;
  --title-blue:#1a9ad6;
  --ink:#1b1b1b;
  --accent-red:#e4261c;
  --rule:#a9abb0;
  --logo-grey:#55585d;
  --photo-a:#d9dee6;
  --photo-b:#b9c3d1;
}
*{margin:0;padding:0;box-sizing:border-box}
html,body{width:1008px;height:1200px;overflow:hidden;background:var(--backdrop)}
.page{
  position:absolute;left:80px;top:0;width:849px;height:1200px;
  background:linear-gradient(to bottom,var(--paper) 0,var(--paper) 1140px,var(--paper-band) 1140px);
  font-family:"Roboto Condensed",Arial,sans-serif;color:var(--ink);
}
.page-title{
  position:absolute;left:58px;top:50px;
  font-family:"Oswald",sans-serif;font-weight:600;font-size:40px;letter-spacing:-0.5px;
  color:var(--title-blue);line-height:1;
}
.team-photo{
  position:absolute;left:58px;top:740px;width:732px;height:390px;
  background:
    linear-gradient(to bottom,var(--paper) 0%,rgba(242,242,244,0) 30%,rgba(242,242,244,0) 75%,var(--paper) 100%),
    linear-gradient(100deg,#d8c8bc 0%,var(--photo-a) 30%,#c8d0dc 55%,#d9c0c0 72%,var(--photo-b) 100%);
}
.testimonials{
  position:absolute;left:58px;top:117px;width:732px;
}
.testimonial{
  font-size:11.8px;line-height:15.4px;text-align:justify;
  padding:14px 0 15px;border-bottom:1px dashed var(--rule);
}
.testimonial:first-child{padding-top:0}
.testimonial:last-child{border-bottom:none}
.testimonial p{margin-bottom:15px}
.testimonial p:last-of-type{margin-bottom:0}
.testimonial p.opening{text-indent:52px}
.attribution{
  display:flex;justify-content:flex-end;align-items:center;gap:7px;
  margin-top:6px;font-size:12px;line-height:16px;font-style:italic;font-weight:700;
}
.attribution::before{content:"";width:48px;height:1px;background:var(--ink);margin-right:4px}
.attribution .name{color:var(--accent-red);font-weight:400}
.attribution .sep{font-style:normal;font-weight:400}
.brand{
  position:absolute;left:0;width:849px;top:1100px;
  display:flex;justify-content:center;align-items:center;gap:12px;
}
.brand-mark{width:30px;height:30px;border-radius:50%;border:3px solid var(--logo-grey)}
.brand-name{font-family:"Montserrat",sans-serif;font-size:26px;font-weight:400;letter-spacing:1px;color:var(--logo-grey)}
.web-address{
  position:absolute;left:0;width:849px;top:1149px;text-align:center;
  font-family:"Montserrat",sans-serif;font-weight:700;font-size:13px;color:var(--accent-red);
}
</style>
</head>
<body>
<main class="page">
  <div class="team-photo" role="img" aria-label="Faded photo of a smiling team meeting around a table with a facilitator standing"></div>

  <h1 class="page-title">TESTIMONIALS</h1>

  <div class="testimonials">
    <section class="testimonial">
      <p class="opening">Our company has worked closely with Warren over the past 24 months. In that time he has taken a detailed, professional, caring approach to developing our leaders as individuals and as a team. Warren is one of those extraordinary individuals who takes the time to understand the true needs of our emerging leaders. His astuteness and professionalism have enabled our leadership team to grasp the fundamentals of life and that of business responsibilities. Warrens personalized care has been the cornerstone to building character and resilience in our staff.</p>
      <p>He has an exceptional strength in relating our cultural values to the personal purposes of our employees. To this end Warren is motivated to find the element that bring out the best in a person and capture the appealing factors that make our people tick. This all leads to building a resilient team of accomplished people who are energetic and driven.</p>
      <p>He is an invaluable partner to our business and key to the future success of our company. I would highly recommend Warren to anyone who's looking to enhance their people and the performance of their business.</p>
      <div class="attribution"><span class="name">Grant</span><span class="sep">|</span><span>Business Owner &amp; Managing Director</span><span class="sep">|</span><span>Construction Industry</span></div>
    </section>

    <section class="testimonial">
      <p class="opening">In less than 6 months working with Warren from Veridian, I have raised my team's game to a whole new level and have learned to delegate more effectively. My relationships with peers, direct reports and key decision-makers have improved greatly, making me a more confident leader. After each session I always walk away with a new, clear, perspective on how to approach my work challenges and a very clear plan of attack. I would strongly recommend Veridian to anyone who is looking to take their leadership to the next level.</p>
      <div class="attribution"><span class="name">Tessa</span><span class="sep">|</span><span>Finance Manager</span><span class="sep">|</span><span>Construction Industry</span></div>
    </section>

    <section class="testimonial">
      <p class="opening">I have found in the past that most professional coaches only provide fluffy solutions to the issues that make you feel good in the short term. Unlike Warren who helped me to identify the issues I was facing that I could not pin point on my own.</p>
      <p>Even after pin pointing the issues, he provided me with the right tools and knowledge that I required to work through the problems and achieve the results I was after.</p>
      <div class="attribution"><span class="name">Reid</span><span class="sep">|</span><span>Operational Manager</span><span class="sep">|</span><span>Construction Industry</span></div>
    </section>

    <section class="testimonial">
      <p class="opening">When I was first referred to Warren at Veridian PD for coaching and mentoring, I was sceptical, stressed and held a very negative outlook on the world. I had been working hard in my own business for over 7 years, but I was miserable and wasn't achieving what I wanted to in life on both a personal and professional level. I knew I wanted to be happy, but I was clouded by constant frustration due to a lack of direction and the everyday issues of life, and I had no idea how to get there.</p>
      <p>Warren helped me understand the importance of purpose, vision and goals. He helped clearly map out where I was heading and where I wanted to go in life, and also helped analyse my personality and the way I view and interact with the world. With his continued support, Warren helped shift my world view and work towards a life with countless opportunities for growth and happiness. My social life and personality is the healthiest and happiest it has ever been, and I now have a clear path and achievable goals. Warren's coaching has helped me harness my greatest strengths and talents in order to unleash my full potential and overcome any goal I set for myself in life, no matter what it is.</p>
      <p>In my opinion, the key to being happy and successful is through continued personal development, and understanding yourself and where you are headed. Both your personal and professional life will flourish... all you need to do is take that first step and be ready to make the change.</p>
      <div class="attribution"><span class="name">Jordan</span><span class="sep">|</span><span>Business Owner</span><span class="sep">|</span><span>Construction Industry</span></div>
    </section>
  </div>

  <div class="brand">
    <span class="brand-mark"></span>
    <span class="brand-name">VERIDIAN PD</span>
  </div>
  <div class="web-address">www.veridianpd.com.au</div>
</main>
</body>
</html>
```